Business Card Design

We have recently seen two business cards that caught our attention and think the designs would work for us. We are an accounting firm that serves small businesses in a variety of industries. Attached are the two business card that inspired us along with very rough layouts. We would like to see a professional layout using our company information.

Industry/Entity Type

Accounting

Contact Information for Business Card

Company Name - Porter Lyle
Address - 4120 Marbury Lane, Suite 310, Houston, TX 77058
713-555-0186 - Main
281-555-0143 - Fax

Team Member Names, emails and phone numbers (see attachment)

```html
<!DOCTYPE html>
<html lang="en">
<head>
<meta charset="utf-8">
<title>Porter Lyle – Business Card</title>
<link rel="stylesheet" href="https://fonts.googleapis.com/css2?family=Exo+2:ital,wght@0,400;0,500;1,400&display=swap">
<style>
  :root {
    --canvas-bg: #e4e4e2;
    --card-white: #f7f7f7;
    --card-shade: #e9e9e9;
    --panel-dark: #3b3b3d;
    --swoosh-grey: #a9a9ab;
    --ink-dark: #3a3a3c;
    --ink-light: #f2f2f2;
    --ink-muted: #cfcfd1;
  }
  * { margin: 0; padding: 0; box-sizing: border-box; }
  html, body { width: 1200px; height: 900px; overflow: hidden; }
  body {
    background: var(--canvas-bg);
    font-family: "Exo 2", sans-serif;
    position: relative;
  }
  .card {
    position: absolute;
    left: 250px;
    width: 700px;
    height: 400px;
    border-radius: 44px;
    overflow: hidden;
    background: linear-gradient(135deg, var(--card-white) 0%, var(--card-shade) 100%);
    box-shadow: 0 10px 28px rgba(0,0,0,0.14);
  }
  .card-front { top: 30px; }
  .card-back { top: 470px; }
  .card-shapes { position: absolute; inset: 0; }

  .wordmark {
    position: absolute;
    display: flex;
    align-items: center;
    gap: 14px;
    color: var(--ink-dark);
    font-weight: 500;
    font-size: 30px;
    letter-spacing: 3px;
    text-transform: uppercase;
  }
  .wordmark-square {
    width: 26px; height: 26px;
    background: var(--ink-dark);
  }
  .card-front .wordmark { left: 40px; top: 178px; }
  .card-back .wordmark { left: 50%; top: 50%; transform: translate(-50%, -50%); font-size: 36px; }
  .card-back .wordmark-square { width: 32px; height: 32px; }

  .person {
    position: absolute;
    left: 430px; top: 58px;
    color: var(--ink-light);
    text-transform: uppercase;
  }
  .person-name { font-size: 24px; font-weight: 500; letter-spacing: 1.5px; }
  .person-title { font-size: 15px; font-style: italic; letter-spacing: 2px; color: var(--ink-muted); margin-top: 2px; }
  .address {
    position: absolute;
    left: 430px; top: 128px;
    width: 240px;
    font-size: 15px;
    line-height: 1.35;
    color: var(--ink-light);
  }
  .contact-list {
    position: absolute;
    left: 400px; top: 212px;
    list-style: none;
    color: var(--ink-muted);
    font-size: 14px;
    letter-spacing: 0.6px;
  }
  .contact-item { display: flex; align-items: center; gap: 12px; height: 30px; }
  .contact-icon { width: 16px; height: 16px; fill: none; stroke: var(--ink-muted); stroke-width: 1.6; stroke-linecap: round; stroke-linejoin: round; }
</style>
</head>
<body>

<section class="card card-front" aria-label="Business card front">
  <svg class="card-shapes" viewBox="0 0 700 400" aria-hidden="true">
    <path d="M402 0 C 352 120, 330 270, 252 400 L232 400 C 312 270, 334 120, 380 0 Z" fill="var(--swoosh-grey)"/>
    <path d="M420 0 C 372 120, 352 270, 276 400 L700 400 L700 0 Z" fill="var(--panel-dark)"/>
  </svg>

  <div class="wordmark"><span class="wordmark-square"></span>Porter Lyle</div>

  <div class="person">
    <div class="person-name">Daniel Hargrove</div>
    <div class="person-title">Financial Advisor</div>
  </div>

  <div class="address">4120 Marbury Lane, Suite 310,<br>Houston, TX 77058</div>

  <ul class="contact-list">
    <li class="contact-item">
      <svg class="contact-icon" viewBox="0 0 16 16"><path d="M3 1.5h3l1.2 3.3-1.8 1.2a8 8 0 0 0 4.6 4.6l1.2-1.8 3.3 1.2v3A1.5 1.5 0 0 1 13 14.5 11.5 11.5 0 0 1 1.5 3 1.5 1.5 0 0 1 3 1.5z"/></svg>
      713-555-0186
    </li>
    <li class="contact-item">
      <svg class="contact-icon" viewBox="0 0 16 16"><rect x="4" y="1.5" width="8" height="4"/><rect x="1.5" y="5.5" width="13" height="6" rx="1"/><rect x="4" y="9.5" width="8" height="5"/></svg>
      281-555-0143
    </li>
    <li class="contact-item">
      <svg class="contact-icon" viewBox="0 0 16 16"><rect x="1.5" y="3" width="13" height="10" rx="1"/><path d="M1.5 4l6.5 5 6.5-5"/></svg>
      dhargrove@porterlyle.com
    </li>
    <li class="contact-item">
      <svg class="contact-icon" viewBox="0 0 16 16"><circle cx="8" cy="8" r="6.5"/><path d="M1.5 8h13M8 1.5c2 2 2.8 4 2.8 6.5S10 12.5 8 14.5C6 12.5 5.2 10.5 5.2 8S6 3.5 8 1.5z"/></svg>
      www.porterlyle.com
    </li>
  </ul>
</section>

<section class="card card-back" aria-label="Business card back">
  <div class="wordmark"><span class="wordmark-square"></span>Porter Lyle</div>
</section>

</body>
</html>
```